Irrigation Business needs their business cards modernised and revamped

I would like to keep my current logo, colours and revamp the format of the card.

I would like the card to be clean yet important.

Im not sure if you include texture but i would like the named logo to be indented into the card etc.

show me something alive and free something thats clinical to the point yet has a feel of achievement. i would like people to go nice card.

Target Market(s)

high end clients, corporate, sports field manger, the guys that make the decisions

Industry/Entity Type

Business

Contact Information for Business Card

nformation to be included

Dorian Hesk (Director)
0487253916
dorian@tfcraft.biz
www.taddsfieldcrafts.com

instagram logo
google logo
facebook logo

Colors

Designer to choose colors to be used in the design.

Requirements
Nice to have
• indentations a really nice feel to the card good texture

```html
<!DOCTYPE html>
<html lang="en">
<head>
<meta charset="utf-8">
<title>Tadd's Field Crafts – Business Card</title>
<link rel="stylesheet" href="https://fonts.googleapis.com/css2?family=Arimo:wght@400;700&display=swap">
<style>
  :root {
    --page-bg: #ececec;
    --card-white: #ffffff;
    --brand-navy: #0d5a86;
    --brand-blue: #2b6fb3;
    --sky-blue: #29a6dc;
    --field-green: #3aa64a;
    --ink-grey: #3d3d3d;
    --icon-tile: #5fa9d6;
  }
  * { box-sizing: border-box; margin: 0; padding: 0; }
  html, body {
    width: 1200px;
    height: 831px;
    overflow: hidden;
    background: var(--page-bg);
    font-family: "Arimo", Arial, sans-serif;
  }
  .business-card {
    position: absolute;
    left: 100px;
    top: 133px;
    width: 1000px;
    height: 565px;
    background: var(--card-white);
    overflow: hidden;
    box-shadow: 0 6px 18px rgba(0,0,0,0.18);
  }
  .footer-band {
    position: absolute;
    left: 0;
    top: 450px;
    width: 1000px;
    height: 115px;
    background: linear-gradient(180deg, var(--sky-blue) 0%, var(--brand-navy) 45%, var(--brand-navy) 100%);
  }
  .brand-block {
    position: absolute;
    left: 68px;
    top: 37px;
    width: 340px;
    text-align: center;
  }
  .brand-mark {
    display: block;
    width: 124px;
    height: 124px;
    margin: 0 auto 12px;
    border-radius: 50%;
    background: var(--brand-blue);
  }
  .brand-name {
    color: var(--brand-blue);
    font-weight: 700;
    font-size: 30px;
    line-height: 36px;
    white-space: nowrap;
  }
  .contact-person {
    position: absolute;
    right: 48px;
    top: 154px;
    text-align: right;
  }
  .person-name {
    color: var(--sky-blue);
    font-weight: 400;
    font-size: 34px;
    letter-spacing: 1px;
    line-height: 38px;
  }
  .person-role {
    color: var(--field-green);
    font-size: 19px;
    letter-spacing: 4px;
    margin-top: 6px;
  }
  .contact-details {
    position: absolute;
    right: 48px;
    top: 337px;
    text-align: right;
    list-style: none;
    color: var(--ink-grey);
    font-size: 24px;
    line-height: 30px;
    letter-spacing: 1px;
  }
  .social-links {
    position: absolute;
    left: 141px;
    top: 495px;
    display: flex;
    gap: 10px;
    list-style: none;
  }
  .social-tile {
    width: 36px;
    height: 36px;
    background: var(--icon-tile);
  }
</style>
</head>
<body>
  <main class="business-card">
    <div class="footer-band" role="img" aria-label="Decorative flowing water band in blue and green"></div>

    <header class="brand-block">
      <span class="brand-mark"></span>
      <p class="brand-name">TADD'S FIELD CRAFTS</p>
    </header>

    <section class="contact-person">
      <h1 class="person-name">DORIAN HESK</h1>
      <p class="person-role">DIRECTOR</p>
    </section>

    <ul class="contact-details">
      <li>0487253916</li>
      <li>dorian@tfcraft.biz</li>
      <li>www.taddsfieldcrafts.com</li>
    </ul>

    <ul class="social-links" aria-label="Social media">
      <li class="social-tile"></li>
      <li class="social-tile"></li>
      <li class="social-tile"></li>
    </ul>
  </main>
</body>
</html>
```